I need a book cover designed for my book entitled Turn Up ~ The Weekly Swatch Project --- This book

I need a book cover designed for this book. I envision the book size being 6x6. This book will take the reader, week by week, over the course of a year, into my journey of going bold through the weekly changing of my nail polish color. The book will contain pictures of the nail polish colors as well as weekly journal entries, monthly summaries and then an overall conlusion that detail the personal discovery and growth that took place through this simple, yet consistent practice of going bold by changing my nail polish.

Reason: I would like to extend the deadline by five days because I have several people looking at the designs and providing their thoughts and a few people have been unable to do so this week! Thank you SO much! Cleo :)

```html
<!DOCTYPE html>
<html lang="en">
<head>
<meta charset="utf-8">
<title>Turn Up! The Weekly Swatch Project</title>
<link rel="stylesheet" href="https://fonts.googleapis.com/css2?family=Anton&family=Bodoni+Moda:opsz,wght@6..96,400&display=swap">
<style>
  :root {
    --maroon: #650d1f;
    --paper: #ffffff;
    --skin-light: #f6c9ae;
    --skin-mid: #eab08f;
    --skin-deep: #d98f6d;
  }
  * { margin: 0; padding: 0; box-sizing: border-box; }
  html, body { width: 1200px; height: 1200px; overflow: hidden; background: var(--paper); }
  .cover { position: relative; width: 1200px; height: 1200px; background: var(--paper); overflow: hidden; }

  .swatch-strip { position: absolute; top: 0; left: 0; width: 1200px; height: 236px; display: flex; gap: 3px; background: var(--paper); }
  .swatch-photo { flex: 1; height: 100%; }
  .swatch-photo--maroon { background: linear-gradient(160deg, #8a1a2b, #4a0a16 60%, #e8c2a8); }
  .swatch-photo--orange { background: linear-gradient(160deg, #f49a6a, #ef5a2a 55%, #f5c4a6); }
  .swatch-photo--yellow { background: linear-gradient(160deg, #f6d23a, #e9e0c0 55%, #f2c9a8); }
  .swatch-photo--green  { background: linear-gradient(160deg, #7cc87a, #a6dc6a 50%, #f0c8a8); }
  .swatch-photo--teal   { background: linear-gradient(160deg, #5fc9cf, #2aa7b3 50%, #f0cbb0); }
  .swatch-photo--blue   { background: linear-gradient(160deg, #2d63c6, #1a3f8e 50%, #d8a95a); }
  .swatch-photo--purple { background: linear-gradient(160deg, #a25ad6, #7b35b8 55%, #f0c4b4); }

  .strip-rule { position: absolute; top: 236px; left: 0; width: 1200px; height: 11px; background: var(--maroon); }

  .title { position: absolute; top: 336px; left: 0; width: 1200px; text-align: center;
    font-family: "Anton", sans-serif; font-size: 268px; line-height: 1; color: var(--maroon);
    text-transform: uppercase; letter-spacing: 2px; }

  .subtitle { position: absolute; top: 600px; left: 0; width: 1200px; text-align: center;
    font-family: "Bodoni Moda", serif; font-weight: 400; font-size: 92px; line-height: 116px;
    color: var(--maroon); letter-spacing: -2px; }

  .hands-photo { position: absolute; left: 0; top: 680px; width: 1200px; height: 520px; }
</style>
</head>
<body>
<main class="cover">
  <div class="swatch-strip">
    <div class="swatch-photo swatch-photo--maroon" role="img" aria-label="Photo of hand with maroon patterned nails"></div>
    <div class="swatch-photo swatch-photo--orange" role="img" aria-label="Photo of hand with orange polka-dot nails"></div>
    <div class="swatch-photo swatch-photo--yellow" role="img" aria-label="Photo of hand with yellow French-tip nails and flowers"></div>
    <div class="swatch-photo swatch-photo--green" role="img" aria-label="Photo of hand with green glitter nails"></div>
    <div class="swatch-photo swatch-photo--teal" role="img" aria-label="Photo of hand with turquoise beaded nails"></div>
    <div class="swatch-photo swatch-photo--blue" role="img" aria-label="Photo of hand with blue jewelled nails"></div>
    <div class="swatch-photo swatch-photo--purple" role="img" aria-label="Photo of hand with purple glitter nails"></div>
  </div>
  <div class="strip-rule"></div>

  <h1 class="title">Turn Up!</h1>
  <p class="subtitle">The Weekly Swatch<br>Project</p>

  <svg class="hands-photo" viewBox="0 0 1200 520" role="img" aria-label="Photo of two hands fanned in an arc, each nail painted a different bright colour">
    <defs>
      <linearGradient id="skin" x1="0" y1="0" x2="0" y2="1">
        <stop offset="0" stop-color="var(--skin-light)"/>
        <stop offset="0.6" stop-color="var(--skin-mid)"/>
        <stop offset="1" stop-color="var(--skin-deep)"/>
      </linearGradient>
    </defs>
    <path d="M0 60 C 200 80, 300 250, 600 250 C 900 250, 1000 60, 1200 30 L1200 520 L0 520 Z" fill="url(#skin)"/>
  </svg>
</main>
</body>
</html>
```